Business cards to launch an education platform

Hi,
I am looking at having new business cards designed.
I am a startup, developing a web platform for schools and university, the education world. It's an online assessment system.
I would like a card that looks classy, and that is using the colors and the font of my logo.

I have attached:
1) my logo
2) A business card that I have designed quickly so you can have all the information required in the card, but I really don't like it.
3) The font that I am using (Lato Regular) to design my web platform
4) Some screenshots of my web platform so you can have a look at the style that I have.

Target Market(s)

Major market: Education system: Schools and university
Minor markets: Business in general

Industry/Entity Type

Business

Contact Information for Business Card

Lydia Marsh
Director

M: 0437 681 902
E: lydia.marsh@copperLeafSystems.com.au

Requirements
Must have
• The colors of my logo

```html
<!DOCTYPE html>
<html lang="en">
<head>
<meta charset="utf-8">
<title>Copperleaf Systems – Business Card</title>
<link href="https://fonts.googleapis.com/css2?family=Lato:wght@300;400;700&display=swap" rel="stylesheet">
<style>
  :root {
    --navy: #1b3864;
    --sky: #2aa3dc;
    --sky-pale: #9fd0f2;
    --ink: #4a4f57;
    --rule: #d9dde2;
    --paper: #ffffff;
    --backdrop: #eceef1;
  }
  * { box-sizing: border-box; margin: 0; padding: 0; }
  html, body {
    width: 1200px; height: 675px; overflow: hidden;
    background: var(--backdrop);
    font-family: "Lato", Arial, sans-serif;
  }
  .canvas {
    width: 1200px; height: 675px;
    display: flex; align-items: center; justify-content: center; gap: 40px;
  }
  .card {
    width: 540px; height: 328px; position: relative; overflow: hidden;
    box-shadow: 0 6px 18px rgba(20, 30, 50, 0.18);
  }

  /* Front */
  .card--front {
    background: var(--navy);
    display: flex; align-items: center; justify-content: center;
  }
  .brand-lockup { display: flex; flex-direction: column; align-items: center; gap: 14px; }
  .brand-mark { display: block; width: 56px; height: 56px; background: var(--sky); }
  .brand-name { color: var(--sky-pale); font-weight: 400; line-height: 1.1; text-align: center; }
  .brand-name__top { display: block; font-size: 30px; letter-spacing: 3px; text-transform: uppercase; }
  .brand-name__bottom { display: block; font-size: 24px; letter-spacing: 3px; }

  /* Back */
  .card--back { background: var(--paper); }
  .back-brand {
    position: absolute; left: 34px; top: 112px; width: 150px;
    display: flex; flex-direction: column; align-items: center; gap: 10px;
  }
  .back-brand .brand-mark { width: 34px; height: 34px; background: var(--navy); }
  .back-brand .brand-name { color: var(--navy); }
  .back-brand .brand-name__top { font-size: 20px; letter-spacing: 1.5px; }
  .back-brand .brand-name__bottom { font-size: 16px; letter-spacing: 1.5px; }
  .divider {
    position: absolute; left: 206px; top: 92px; width: 1px; height: 116px;
    background: var(--rule);
  }
  .contact { position: absolute; left: 232px; top: 100px; }
  .contact__name { color: var(--navy); font-size: 22px; font-weight: 400; }
  .contact__role { color: var(--sky); font-size: 13px; margin-top: 1px; }
  .contact__list { list-style: none; margin-top: 20px; }
  .contact__item {
    display: flex; align-items: center; gap: 9px;
    color: var(--ink); font-size: 14px; line-height: 23px;
  }
  .contact__item svg { width: 12px; height: 12px; flex: none; }
  .base-line {
    position: absolute; left: 0; bottom: 18px; width: 100%; height: 3px;
    background: var(--sky);
  }
  .base-bar {
    position: absolute; left: 0; bottom: 0; width: 100%; height: 12px;
    background: var(--navy);
  }
</style>
</head>
<body>
<main class="canvas">
  <section class="card card--front" aria-label="Card front">
    <div class="brand-lockup">
      <span class="brand-mark"></span>
      <p class="brand-name">
        <span class="brand-name__top">Copperleaf</span>
        <span class="brand-name__bottom">Systems</span>
      </p>
    </div>
  </section>

  <section class="card card--back" aria-label="Card back">
    <div class="back-brand">
      <span class="brand-mark"></span>
      <p class="brand-name">
        <span class="brand-name__top">COPPERLEAF</span>
        <span class="brand-name__bottom">Systems</span>
      </p>
    </div>
    <div class="divider"></div>
    <div class="contact">
      <h1 class="contact__name">Lydia Marsh</h1>
      <p class="contact__role">Director</p>
      <ul class="contact__list">
        <li class="contact__item">
          <svg viewBox="0 0 12 12" aria-hidden="true"><rect x="3" y="0.5" width="6" height="11" rx="1" fill="none" stroke="var(--sky)" stroke-width="1.2"/><circle cx="6" cy="9.5" r="0.7" fill="var(--sky)"/></svg>
          0437 681 902
        </li>
        <li class="contact__item">
          <svg viewBox="0 0 12 12" aria-hidden="true"><rect x="0.5" y="2" width="11" height="8" fill="var(--sky)"/><path d="M0.5 2 L6 6.5 L11.5 2" fill="none" stroke="#fff" stroke-width="1"/></svg>
          lydia.marsh@copperLeafSystems.com.au
        </li>
        <li class="contact__item">
          <svg viewBox="0 0 12 12" aria-hidden="true"><g fill="none" stroke="var(--sky)" stroke-width="1"><circle cx="6" cy="6" r="5.2"/><ellipse cx="6" cy="6" rx="2.3" ry="5.2"/><path d="M0.8 6 H11.2 M1.8 3.3 H10.2 M1.8 8.7 H10.2"/></g></svg>
          www.copperLeafSystems.com.au
        </li>
      </ul>
    </div>
    <div class="base-line"></div>
    <div class="base-bar"></div>
  </section>
</main>
</body>
</html>
```